Tolvek Card Design

IT consulting services - my company focuses on delivering value add for clients through sourcing services, strategic and project consulting services, as well as delivering office fitout project managment services.
We also offer IT Interim managment services - to fill the gap when looking for executive roles.
I use orange and blue as my corporate colours
I am after a simple design with my details on the front and my services not the back
Industry/Entity Type
It Company
Contact Information for Business Card
Martin Oskrey
Director
Tolvek Solutions
Martin.Oskrey@TolvekSolutions.com.au
www.TolvekSolutions.com.au
m: +61 427580916
On Rear of card:
Interim Management
Project and Strategy Consulting
Sourcing Services
Commercial fit-out management

```html
<!DOCTYPE html>
<html lang="en">
<head>
<meta charset="utf-8">
<title>Tolvek Card Design</title>
<link href="https://fonts.googleapis.com/css2?family=Open+Sans:wght@400;600;700&display=swap" rel="stylesheet">
<style>
  :root {
    --navy: #17386b;
    --orange: #f39c12;
    --ink: #3a3a3a;
    --card: #f7f7f7;
    --card-shade: #e9e9e9;
    --backdrop: #d9d6d1;
  }
  * { margin: 0; padding: 0; box-sizing: border-box; }
  html, body { width: 1200px; height: 828px; overflow: hidden; }
  body {
    background: var(--backdrop);
    font-family: "Open Sans", Arial, sans-serif;
    position: relative;
  }
  .card {
    position: absolute;
    width: 540px;
    height: 310px;
    background: linear-gradient(135deg, #ffffff 0%, var(--card) 55%, var(--card-shade) 100%);
    box-shadow: 0 6px 18px rgba(0,0,0,0.18);
    overflow: hidden;
  }
  .card-front { left: 80px; top: 100px; }
  .card-back { left: 580px; top: 430px; }

  .brand {
    display: flex;
    align-items: center;
    gap: 10px;
    white-space: nowrap;
  }
  .brand-square {
    width: 26px; height: 26px;
    background: var(--orange);
    flex: none;
  }
  .brand-name {
    font-weight: 700;
    color: var(--navy);
    white-space: nowrap;
  }
  .card-front .brand {
    position: absolute;
    left: 50%; top: 50%;
    transform: translate(-50%, -50%);
  }
  .card-front .brand-name { font-size: 30px; }
  .card-front .brand-square { width: 32px; height: 32px; }

  .swoosh { position: absolute; right: 0; top: 0; }

  .person {
    position: absolute;
    right: 85px; top: 100px;
    text-align: right;
    white-space: nowrap;
  }
  .person-name { color: var(--orange); font-weight: 700; font-size: 15px; }
  .person-role { color: var(--ink); font-size: 13px; margin-top: 1px; }

  .card-back .brand {
    position: absolute;
    left: 40px; top: 150px;
  }
  .card-back .brand-name { font-size: 24px; }

  .contact {
    position: absolute;
    left: 40px; top: 198px;
    color: var(--ink);
    font-size: 11px;
    line-height: 1.45;
    white-space: nowrap;
  }
  .contact-address { margin-bottom: 5px; }
  .contact-list { list-style: none; }
  .contact-list li { display: flex; align-items: center; gap: 7px; }
  .contact-list svg { width: 10px; height: 10px; flex: none; }
</style>
</head>
<body>

<div class="card card-front">
  <div class="brand">
    <span class="brand-square"></span>
    <span class="brand-name">Tolvek Solution</span>
  </div>
</div>

<div class="card card-back">
  <svg class="swoosh" width="540" height="310" viewBox="0 0 540 310">
    <path d="M300 0 C400 15 490 70 540 150 L540 0 Z" fill="var(--navy)"/>
    <path d="M288 0 C388 17 478 74 530 156" fill="none" stroke="var(--orange)" stroke-width="5"/>
  </svg>

  <div class="person">
    <div class="person-name">Dalia Fenwick-Orr</div>
    <div class="person-role">Consultant</div>
  </div>

  <div class="brand">
    <span class="brand-square"></span>
    <span class="brand-name">Tolvek Solution</span>
  </div>

  <div class="contact">
    <p class="contact-address">041,12th floor, Quay<br>Harbour Road KLD</p>
    <ul class="contact-list">
      <li>
        <svg viewBox="0 0 10 10"><path d="M2 1h2l1 2.5-1.2 1a5 5 0 0 0 1.7 1.7l1-1.2L9 6v2a1 1 0 0 1-1 1A7 7 0 0 1 1 2a1 1 0 0 1 1-1z" fill="var(--orange)"/></svg>
        034 567 8912
      </li>
      <li>
        <svg viewBox="0 0 10 10"><rect x="2.5" y="0.5" width="5" height="9" rx="1" fill="var(--orange)"/></svg>
        034 567 8912
      </li>
      <li>
        <svg viewBox="0 0 10 10"><rect x="0.5" y="2" width="9" height="6" fill="var(--orange)"/><path d="M0.5 2l4.5 3.5L9.5 2" fill="none" stroke="#fff" stroke-width="0.8"/></svg>
        hello@tolvekmail.com
      </li>
      <li>
        <svg viewBox="0 0 10 10"><circle cx="5" cy="5" r="4.5" fill="var(--orange)"/></svg>
        www.tolvekweb.com
      </li>
    </ul>
  </div>
</div>

</body>
</html>
```